Catering Company Needs a Web Page Design

I already have my logo, and so I'm moving onto the next phase.. the web page design. Zestora is a gourmet catering company based in orlando, fl, set to launch in 2015. I will have a store location to host cooking classes as well.... and will be uploading cooking demo videos to my website weekly. Id like a blog section, and about, a video section, contact form, Services, Menu Samples..... My logo and concept is modern, innovative, and fun! I am targeting middle class to upper middle class women, but i want the site to be super unique.

Industry/Entity Type

Catering

Requirements
Must have
• The front/main page must have the logo... and the quillnote registry's definition of "zestora". I like movement... maybe the top banner can move somehow.. Im not a web designer, so i wont really know until I start seeing some examples. For now I dont have photos of my own cooking, so if you could use stock photos of catering dishes.. I uploaded a transparent logo also, maybe that could be the top banner placed over a scene of expertly plated hordourves...

```html
<!DOCTYPE html>
<html lang="en">
<head>
<meta charset="utf-8">
<title>Zestora — Contact</title>
<link rel="stylesheet" href="https://fonts.googleapis.com/css2?family=Noto+Sans:wght@400;700;800&display=swap">
<style>
  :root {
    --ink: #111111;
    --text: #4a4a4a;
    --muted: #555555;
    --tagline: #7a7a7a;
    --field-border: #7a7a7a;
    --rule: #2e2e2e;
    --button: #333333;
    --footer: #363636;
    --white: #ffffff;
  }
  * { box-sizing: border-box; margin: 0; padding: 0; }
  html, body {
    width: 1200px; height: 570px; overflow: hidden;
    background: var(--white);
    font-family: "Noto Sans", Verdana, sans-serif;
  }
  .page { position: relative; width: 1200px; height: 570px; }

  .top-rule { position: absolute; left: 148px; top: 0; width: 904px; height: 2px; background: var(--rule); }

  .brand { position: absolute; left: 188px; top: 12px; width: 230px; }
  .brand-name {
    font-size: 54px; font-weight: 800; color: var(--ink);
    letter-spacing: -1px; line-height: 68px;
  }
  .brand-tagline {
    position: absolute; left: 52px; top: 67px;
    font-size: 10px; color: var(--tagline); white-space: nowrap;
  }

  .main-nav { position: absolute; top: 45px; left: 0; width: 1200px; height: 30px; }
  .main-nav a {
    position: absolute; font-size: 19px; color: var(--ink);
    text-decoration: none; white-space: nowrap;
  }

  .contact-form label {
    position: absolute; left: 212px; font-size: 24px; color: var(--text);
  }
  .field {
    position: absolute; border: 1px solid var(--field-border); background: var(--white);
    font: inherit;
  }
  .field-name { left: 289px; top: 129px; width: 323px; height: 36px; }
  .field-email { left: 289px; top: 173px; width: 323px; height: 36px; }
  .field-message { left: 320px; top: 217px; width: 292px; height: 133px; resize: none; }
  .send-button {
    position: absolute; left: 515px; top: 357px; width: 97px; height: 39px;
    background: var(--button); color: var(--white); border: none;
    font: 19px "Noto Sans", Verdana, sans-serif; line-height: 37px;
  }

  .address { position: absolute; left: 689px; top: 125px; color: var(--muted); font-style: normal; }
  .address-title { font-size: 24px; line-height: 30px; }
  .address-line { font-size: 18px; line-height: 20.7px; }

  .site-footer { position: absolute; left: 0; top: 452px; width: 1200px; height: 118px; background: var(--footer); }
  .social-links { position: absolute; left: 502px; top: 30px; display: flex; gap: 11px; }
  .social-link { display: block; width: 41px; height: 41px; border-radius: 50%; background: var(--white); }
</style>
</head>
<body>
<div class="page">
  <div class="top-rule"></div>

  <header>
    <div class="brand">
      <div class="brand-name">zestora</div>
      <div class="brand-tagline">Gourmet Catering &amp; Cooking Classes</div>
    </div>
    <nav class="main-nav">
      <a href="#" style="left:485px">about</a>
      <a href="#" style="left:560px">services</a>
      <a href="#" style="left:654px">menu samples</a>
      <a href="#" style="left:808px">video</a>
      <a href="#" style="left:877px">blog</a>
      <a href="#" style="left:936px">contact</a>
    </nav>
  </header>

  <form class="contact-form">
    <label for="name" style="top:128px">name</label>
    <input id="name" class="field field-name" type="text">
    <label for="email" style="top:174px">e-mail</label>
    <input id="email" class="field field-email" type="email">
    <label for="message" style="top:213px">message</label>
    <textarea id="message" class="field field-message"></textarea>
    <button class="send-button" type="button">send</button>
  </form>

  <address class="address">
    <div class="address-title">zestora</div>
    <div class="address-line">address line 1</div>
    <div class="address-line">cedar bay, alvona</div>
    <div class="address-line">0800 xxx xxx</div>
    <div class="address-line">contact@zestora.com</div>
  </address>

  <footer class="site-footer">
    <div class="social-links">
      <a href="#" class="social-link" aria-label="Social profile 1"></a>
      <a href="#" class="social-link" aria-label="Social profile 2"></a>
      <a href="#" class="social-link" aria-label="Video channel"></a>
      <a href="#" class="social-link" aria-label="Social profile 3"></a>
    </div>
  </footer>
</div>
</body>
</html>
```